Bref créative
Dravel & Partners
Global Medical Device Regulatory Affairs and Quality Specialist
Professional
Merrin T. Halvorsen
President
14 Quarry Mill Road
Cicero, IN 46108
merrinhalvorsen@dravelandpart.example
www.dravelandpart.example
Please visit our website at http://dravelandpart.example/default.php# to see colors needed to be used in design.
Logo and subtitle with web address(this information should also be on the front of the card.)

```html
<!DOCTYPE html>
<html lang="en">
<head>
<meta charset="utf-8">
<title>Dravel &amp; Partners — Business Card</title>
<link rel="stylesheet" href="https://fonts.googleapis.com/css2?family=Cinzel:wght@600;700&family=Crimson+Text:wght@400;600&family=Open+Sans:wght@600;700&display=swap">
<style>
  :root {
    --page-bg: #e4e4e6;
    --card-white: #ffffff;
    --brand-purple: #3a2a6c;
    --brand-purple-deep: #2c1f57;
    --brand-gold: #c9a14a;
    --brand-gold-light: #e3c67e;
    --ink-dark: #2b2b2e;
    --ink-light: #ffffff;
    --rule-grey: #b9b9be;
  }
  * { box-sizing: border-box; margin: 0; padding: 0; }
  html, body {
    width: 1200px; height: 780px; overflow: hidden;
    background: var(--page-bg);
  }
  .business-card {
    position: absolute; left: 50px; top: 75px;
    width: 1100px; height: 630px;
    border-radius: 42px; overflow: hidden;
    background: var(--card-white);
    box-shadow: 0 10px 30px rgba(0,0,0,0.18);
  }
  .card-swoosh { position: absolute; inset: 0; width: 1100px; height: 630px; }

  .brand-mark {
    position: absolute; left: 245px; top: 72px;
    width: 170px; height: 170px; border-radius: 50%;
    background: var(--brand-purple);
  }
  .brand-divider {
    position: absolute; left: 438px; top: 80px;
    width: 2px; height: 150px; background: var(--brand-gold);
  }
  .brand-name {
    position: absolute; left: 458px; top: 80px;
    font-family: "Cinzel", serif; font-weight: 700;
    font-size: 60px; line-height: 1; color: var(--ink-dark);
    letter-spacing: 1px; white-space: nowrap;
  }
  .brand-tagline {
    position: absolute; left: 462px; top: 158px;
    font-family: "Cinzel", serif; font-weight: 700;
    font-size: 15.5px; color: var(--ink-dark);
    letter-spacing: 0.4px; white-space: nowrap;
  }

  .contact-list {
    position: absolute; left: 62px; top: 440px;
    list-style: none;
    font-family: "Crimson Text", serif; font-size: 24px;
    color: var(--ink-light); line-height: 38px;
  }
  .contact-list li { display: flex; align-items: center; gap: 9px; white-space: nowrap; }
  .contact-list .phone-pair { gap: 9px; }
  .contact-list .phone-pair .spacer { width: 14px; }
  .contact-icon { width: 20px; height: 20px; flex: none; }

  .person {
    position: absolute; right: 70px; top: 452px; text-align: right;
    font-family: "Open Sans", sans-serif; color: var(--ink-light);
  }
  .person-name { font-size: 28px; font-weight: 700; line-height: 1.2; }
  .person-title { font-size: 20px; font-weight: 600; line-height: 1.3; }
</style>
</head>
<body>
  <div class="business-card">
    <svg class="card-swoosh" viewBox="0 0 1100 630" aria-hidden="true">
      <defs>
        <linearGradient id="goldSweep" x1="0" y1="0" x2="1" y2="0">
          <stop offset="0" stop-color="var(--brand-gold)"/>
          <stop offset="0.5" stop-color="var(--brand-gold-light)"/>
          <stop offset="1" stop-color="var(--brand-gold)"/>
        </linearGradient>
        <linearGradient id="purpleField" x1="0" y1="0" x2="0" y2="1">
          <stop offset="0" stop-color="var(--brand-purple)"/>
          <stop offset="1" stop-color="var(--brand-purple-deep)"/>
        </linearGradient>
      </defs>
      <path d="M0 318 C 300 250, 650 300, 1100 222" fill="none" stroke="var(--rule-grey)" stroke-width="2"/>
      <path d="M0 335 C 300 262, 650 312, 1100 236 L1100 292 C 700 338, 350 298, 0 372 Z" fill="url(#goldSweep)"/>
      <path d="M0 372 C 350 302, 700 346, 1100 290 L1100 630 L0 630 Z" fill="url(#purpleField)"/>
    </svg>

    <div class="brand-mark"></div>
    <div class="brand-divider"></div>
    <div class="brand-name">Dravel &amp; Partners</div>
    <div class="brand-tagline">Global Medical Device Regulatory Affairs &amp; Quality Specialist</div>

    <ul class="contact-list">
      <li>14 Quarry Mill Road Cicero, IN 46108</li>
      <li class="phone-pair">
        <svg class="contact-icon" viewBox="0 0 20 20" aria-hidden="true"><path d="M5 2 L8 2 L9 6 L7 8 C8 11 9 12 12 13 L14 11 L18 12 L18 15 C18 17 16 18 14 18 C8 17 3 12 2 6 C2 4 3 2 5 2 Z" fill="var(--ink-light)"/></svg>
        <span>(317)555-0142</span>
        <span class="spacer"></span>
        <svg class="contact-icon" viewBox="0 0 20 20" aria-hidden="true"><rect x="5" y="1" width="10" height="18" rx="2" fill="var(--ink-light)"/><rect x="7" y="3.5" width="6" height="10" fill="var(--brand-purple)"/></svg>
        <span>(317)555-0187</span>
      </li>
      <li>
        <svg class="contact-icon" viewBox="0 0 20 20" aria-hidden="true"><circle cx="10" cy="10" r="9" fill="var(--ink-light)"/><text x="10" y="14.5" text-anchor="middle" font-size="13" font-family="Open Sans, sans-serif" font-weight="700" fill="var(--brand-purple)">@</text></svg>
        <span>merrinhalvorsen@dravelandpart.example</span>
      </li>
      <li>
        <svg class="contact-icon" viewBox="0 0 20 20" aria-hidden="true"><circle cx="10" cy="10" r="9" fill="var(--ink-light)"/><ellipse cx="10" cy="10" rx="4" ry="8" fill="none" stroke="var(--brand-purple)" stroke-width="1.4"/><line x1="2" y1="10" x2="18" y2="10" stroke="var(--brand-purple)" stroke-width="1.4"/></svg>
        <span>www.dravelandpart.example</span>
      </li>
    </ul>

    <div class="person">
      <div class="person-name">Merrin T. Halvorsen</div>
      <div class="person-title">President</div>
    </div>
  </div>
</body>
</html>
```